Political sign design, fonts colors and layout

I am running for Town Council.

My message is done, and *a draft is attached* with the text we wish to use. It says "Elect Dana Velmont" etc. In Maroon and White. I am not a designer, but this is somewhat close to what we are looking for.

I need help with colors and fonts, layout, spacing, and general cleanup.

I'm attaching the town high school logo:

- "H" for Brookfield: with black and white outlines on the fonts
- we want to incorporate the black and white on the fonts
- for the entire text, parts of the text, or best would be a mix

This is for signs printed and placed all over my town.

We need two versions

1. square, 4' by 4' version
2. 36" by 24" version

The smaller version will drop the three bullet pointed text, but otherwise can be identical.

The sign can only use 3 printed colors (due to printing costs.)

1. maroon,
2. white,
3. black.

The maroon should match the maroon from the high school logo attached, which I believe I did in the draft.

We also like the white border around the outside, like in the "scoreboard" design attached.

Thanks for your attention, wish me luck.

Dana

Target Market(s)

SIgns, Political market

Industry/Entity Type

Political

Font styles to use
Sans Serif
Other font styles liked:
• Arial Black, Sans Serif Bold

Requirements
Must have
• maroon background, white font.
• - black borders around fonts where appropriate
• - great spacing
• - great typeface usage
• - clean and crisp political sign, visible while driving.
• - my name "Dana Velmont" much larger like the draft, or the appropriate additional size
• - two versions, one square, and one 36" / 24"
Nice to have
• - nice borders
• - dress it up a bit, using italics and bold fonts, without making it flashy or busy.
Should not have
• Must be easily readable from a car, except for "Paid for by Friends of Dana Velmont" which can be tiny.
• Colors are noted in the description, the "Brookfield Maroon" as the background, white font, and some use of black.

```html
<!DOCTYPE html>
<html lang="en">
<head>
<meta charset="utf-8">
<title>Elect Dana Velmont – Brookfield Council Sign</title>
<link href="https://fonts.googleapis.com/css2?family=Montserrat:ital,wght@0,400;0,500;0,700;0,800;1,700;1,800&display=swap" rel="stylesheet">
<style>
  :root {
    --brookfield-maroon: #690a2c;
    --sign-white: #ffffff;
    --sign-black: #000000;
  }
  html, body {
    margin: 0;
    padding: 0;
    width: 1200px;
    height: 1200px;
    overflow: hidden;
    background: var(--brookfield-maroon);
  }
  .sign {
    display: block;
    width: 1200px;
    height: 1200px;
    font-family: "Montserrat", Arial, sans-serif;
  }
  .sign-field { fill: var(--brookfield-maroon); }
  .frame-white { fill: var(--sign-white); }
  .frame-black { fill: var(--sign-black); }
  .plain-text { fill: var(--sign-white); }
  .headline-elect { font-size: 100px; font-weight: 400; }
  .headline-name { font-size: 90px; font-weight: 800; }
  .office { font-size: 50px; font-weight: 500; }
  .slogan { font-size: 72px; font-weight: 800; font-style: italic; font-variant: small-caps; letter-spacing: 1px; }
  .tagline { font-size: 56px; font-weight: 500; }
  .platform-item { font-size: 60px; font-weight: 500; }
  .vote-word { font-size: 100px; font-weight: 800; font-style: italic; letter-spacing: -2px; }
  .vote-date { font-size: 56px; font-weight: 500; }
  .website { font-size: 48px; font-weight: 700; }
  .disclaimer { font-size: 28px; font-weight: 500; }
  .outline-halo { fill: none; stroke: var(--sign-white); stroke-width: 20px; stroke-linejoin: round; }
  .outline-core { fill: none; stroke: var(--sign-black); stroke-width: 14px; stroke-linejoin: round; }
  .outline-fill { fill: var(--sign-white); }
  .checkbox { fill: none; stroke: var(--sign-white); stroke-width: 3.5; }
  .checkmark { fill: none; stroke: var(--sign-white); stroke-width: 4; stroke-linecap: round; stroke-linejoin: round; }
</style>
</head>
<body>
<svg class="sign" viewBox="0 0 1200 1200" xmlns="http://www.w3.org/2000/svg" aria-label="Elect Dana Velmont for Brookfield Councilman/Trustee">
  <!-- frame -->
  <rect class="sign-field" x="0" y="0" width="1200" height="1200"/>
  <rect class="frame-white" x="18" y="18" width="1164" height="1164"/>
  <rect class="frame-black" x="40" y="40" width="1120" height="1120"/>
  <rect class="sign-field" x="58" y="58" width="1084" height="1084"/>

  <!-- headline -->
  <g class="headline">
    <text class="plain-text headline-elect" x="104" y="188">Elect</text>
    <g class="headline-name">
      <text class="outline-halo" x="384" y="188">Dana Velmont</text>
      <text class="outline-core" x="384" y="188">Dana Velmont</text>
      <text class="outline-fill" x="384" y="188">Dana Velmont</text>
    </g>
  </g>
  <text class="plain-text office" x="600" y="264" text-anchor="middle">for Brookfield Councilman/Trustee</text>

  <!-- slogan -->
  <text class="plain-text slogan" x="600" y="404" text-anchor="middle">Take Back Our Town!</text>
  <text class="plain-text tagline" x="600" y="488" text-anchor="middle">Fighting for Brookfield</text>

  <!-- platform -->
  <g class="platform">
    <g transform="translate(134 584)">
      <rect class="checkbox" x="0" y="6" width="34" height="34"/>
      <path class="checkmark" d="M7 22 L16 32 L40 0"/>
    </g>
    <text class="plain-text platform-item" x="194" y="625">Stop HIGH Taxes</text>

    <g transform="translate(134 667)">
      <rect class="checkbox" x="0" y="6" width="34" height="34"/>
      <path class="checkmark" d="M7 22 L16 32 L40 0"/>
    </g>
    <text class="plain-text platform-item" x="194" y="708">Clean up our government</text>

    <g transform="translate(134 749)">
      <rect class="checkbox" x="0" y="6" width="34" height="34"/>
      <path class="checkmark" d="M7 22 L16 32 L40 0"/>
    </g>
    <text class="plain-text platform-item" x="194" y="790">Preserve our neighborhoods</text>
  </g>

  <!-- call to vote -->
  <g class="call-to-vote">
    <text class="outline-halo vote-word" x="212" y="962">Vote</text>
    <text class="outline-core vote-word" x="212" y="962">Vote</text>
    <text class="outline-fill vote-word" x="212" y="962">Vote</text>
    <text class="plain-text vote-date" x="482" y="962">Nov. 8th “Row A”</text>
  </g>

  <!-- footer -->
  <text class="plain-text website" x="88" y="1112">www.votedana.com</text>
  <text class="plain-text disclaimer" x="1115" y="1108" text-anchor="end">Paid for by friends of Dana Velmont</text>
</svg>
</body>
</html>
```